Web Design for an Online Dating Web Site

We need an uncoded web design for a new online dating web site called zMatchy.net. Simplicity and boldness are the key factors in the successful design.
Please look at the requirements document attached for details.
Updates
Dear all,
Please AVOID USING A PICTURE OF A HAPPY COUPLE ON THE HOME PAGE of the site. We highly want to move away from this space as it makes our web site just like another dating web site.
We like something simple with web 2.0 look and feel. The examples in the Requirements Document are exactly the design we are after.
Regards
Tarn
Industry/Entity Type
Dating
Look and feel
Each slider illustrates characteristics of the customer's brand and the style your logo design should communicate.

```html
<!DOCTYPE html>
<html lang="en">
<head>
<meta charset="utf-8">
<title>zMatchy.net – Home</title>
<link href="https://fonts.googleapis.com/css2?family=Questrial&family=Arimo:wght@400;700&display=swap" rel="stylesheet">
<style>
:root{
  --pink-top:#dc48a6;
  --pink-main:#ec88cc;
  --pink-deep:#d23a9c;
  --pink-band:#f04fb2;
  --pink-input:#de3398;
  --magenta:#e0168a;
  --lime:#bbdf0e;
  --lime-light:#e6f59a;
  --lime-dark:#98b80a;
  --olive:#4f6a00;
  --ink:#1c1c1c;
  --white:#ffffff;
}
*{box-sizing:border-box;margin:0;padding:0}
html,body{width:1200px;height:1118px;overflow:hidden}
body{font-family:"Arimo",Arial,sans-serif;background:var(--pink-main);position:relative}
.page{position:absolute;inset:0;width:1200px;height:1118px;overflow:hidden}
.hero{position:absolute;left:0;top:0;width:1200px;height:872px;
  background:linear-gradient(to bottom,var(--pink-top) 0,var(--pink-main) 150px,var(--pink-main) 100%)}
.brand{position:absolute;left:0;top:28px;width:1200px;text-align:center;
  font-family:"Questrial",sans-serif;font-size:54px;color:var(--white);letter-spacing:1px}
.brand .dot{display:inline-block;width:16px;height:16px;border-radius:50%;background:var(--magenta);margin-left:8px;vertical-align:middle}
.nav{position:absolute;left:141px;top:135px;width:919px;height:46px;border-radius:6px;display:flex;
  background:linear-gradient(to bottom,var(--lime-light) 0,#cfe84a 48%,var(--lime) 52%,var(--lime) 100%);
  box-shadow:2px 3px 4px rgba(120,30,90,.35);overflow:hidden}
.nav a{display:flex;align-items:center;justify-content:center;height:46px;text-decoration:none;
  font-family:"Arimo",sans-serif;font-weight:700;font-size:15px;color:var(--ink);border-right:1px solid var(--lime-dark)}
.nav a.current{background:linear-gradient(to bottom,#e66ab8 0,#e050a8 48%,var(--magenta) 52%,#d01a88 100%);color:var(--white)}
.intro{position:absolute;left:258px;top:232px;width:652px;color:var(--white)}
.intro h1{font-family:"Questrial",sans-serif;font-weight:400;font-size:39px;letter-spacing:-1px;white-space:nowrap}
.intro p{margin-top:20px;font-size:11px;line-height:15.5px}
.btn-signup{position:absolute;left:718px;top:349px;width:191px;height:52px;border-radius:14px;
  border:4px solid #c8e437;background:linear-gradient(to bottom,#f0fbb4 0,#cde94a 55%,#b5d50e 100%);
  display:flex;align-items:center;justify-content:center;font-size:24px;color:var(--ink);box-shadow:inset 0 0 0 2px #eaf7a8}
.stage{position:absolute;left:0;top:410px}
.screenshot{position:absolute;left:421px;top:485px;width:387px;height:325px;
  background:linear-gradient(to bottom,var(--pink-deep) 0,var(--pink-deep) 80%,rgba(210,58,156,0) 100%)}
.slider-dots{position:absolute;left:543px;top:838px;display:flex;gap:14px}
.slider-dots span{width:11px;height:11px;border-radius:50%;background:var(--magenta)}
.slider-dots span.active{background:var(--lime)}
.login-band{position:absolute;left:0;top:872px;width:1200px;height:106px;background:var(--pink-band);border-top:1px solid #d8409c}
.field{position:absolute;top:32px;height:43px;width:207px;border-radius:6px;border:1px solid #7a1450;
  background:var(--pink-input);color:#f8c6e6;font-size:15px;padding-left:19px;display:flex;align-items:center;box-shadow:inset 0 0 0 1px #f07cc6}
.btn-login{position:absolute;left:581px;top:31px;width:116px;height:45px;border-radius:7px;
  background:linear-gradient(to bottom,#eef9b0 0,#cde94a 55%,#b5d50e 100%);display:flex;align-items:center;justify-content:center;
  font-size:19px;color:var(--ink);box-shadow:2px 3px 3px rgba(110,20,70,.35)}
.or{position:absolute;left:713px;top:45px;color:var(--white);font-size:18px}
.networks{position:absolute;top:39px;display:flex;gap:10px}
.network{width:34px;height:30px;border-radius:4px;display:flex;align-items:center;justify-content:center;white-space:nowrap;
  font-size:8px;font-weight:700;color:var(--white);background:rgba(255,255,255,.18)}
.btn-more{position:absolute;left:977px;top:40px;width:78px;height:30px;border-radius:5px;
  background:linear-gradient(to bottom,#eef9b0 0,#c8e63a 60%,#b5d50e 100%);font-size:13px;color:var(--ink);
  display:flex;align-items:center;justify-content:center;gap:10px;box-shadow:1px 2px 3px rgba(110,20,70,.3)}
.btn-more i{width:11px;height:11px;border-radius:50%;border:1px solid var(--ink);font-style:normal;font-size:10px;line-height:9px;text-align:center}
.footer{position:absolute;left:0;top:978px;width:1200px;height:140px;background:var(--lime)}
.footer-brand{position:absolute;left:143px;top:24px;font-family:"Questrial",sans-serif;font-size:34px;color:var(--olive)}
.footer-networks{position:absolute;right:141px;top:34px;display:flex;gap:9px}
.footer-networks .network{background:var(--olive);width:30px;height:32px;font-size:7.5px}
.footer-rule{position:absolute;left:141px;top:92px;width:919px;height:1px;background:#a6c60c}
.copyright{position:absolute;left:143px;top:108px;font-size:10.5px;color:var(--ink)}
.footer-links{position:absolute;right:141px;top:109px;display:flex;gap:17px;font-size:10.5px}
.footer-links a{color:var(--ink);text-decoration:none}
</style>
</head>
<body>
<div class="page">
  <header class="hero">
    <div class="brand">zMatchy.net<span class="dot"></span></div>
    <nav class="nav">
      <a class="current" href="#" style="width:93px">Home</a>
      <a href="#" style="width:81px">Why</a>
      <a href="#" style="width:147px">How It Works</a>
      <a href="#" style="width:104px">Sign Up</a>
      <a href="#" style="width:118px">Our Blog</a>
    </nav>
    <section class="intro">
      <h1>Lorem ipsum dolor sit amet consecutor</h1>
      <p>Lorem ipsum dolor sit amet consecutor. Lorem ipsum dolor sit amet consecutor. Lorem ipsum dolor sit amet consecutor. Lorem ipsum dolor sit amet consecutor. Lorem ipsum dolor sit amet consecutor. Lorem ipsum dolor sit amet consecutor. Lorem ipsum dolor sit amet consecutor.</p>
    </section>
    <a class="btn-signup">Sign Up</a>
    <svg class="stage" width="1200" height="420" viewBox="0 0 1200 420" aria-hidden="true">
      <defs>
        <linearGradient id="arcFade" x1="0" y1="0" x2="0" y2="1">
          <stop offset="0" stop-color="#e070b8" stop-opacity=".9"/>
          <stop offset="1" stop-color="#ec88cc" stop-opacity="0"/>
        </linearGradient>
      </defs>
      <path d="M150 180 Q600 -120 1055 180 L1055 320 L150 320 Z" fill="url(#arcFade)"/>
    </svg>
    <div class="screenshot" role="img" aria-label="Product screenshot carousel slide"></div>
    <div class="slider-dots"><span class="active"></span><span></span><span></span><span></span><span></span></div>
  </header>

  <section class="login-band">
    <div class="field" style="left:143px">Email Address</div>
    <div class="field" style="left:363px">Password</div>
    <a class="btn-login">Login</a>
    <span class="or">OR</span>
    <div class="networks" style="left:750px">
      <span class="network">Fabo</span>
      <span class="network">Posti</span>
      <span class="network">Yodl</span>
      <span class="network">Keyo</span>
      <span class="network">Spaco</span>
    </div>
    <a class="btn-more">More <i>+</i></a>
  </section>

  <footer class="footer">
    <div class="footer-brand">zMatchy.net</div>
    <div class="footer-networks">
      <span class="network">Fabo</span>
      <span class="network">Chirp</span>
      <span class="network">Wandr</span>
      <span class="network">Spaco</span>
      <span class="network">Yodl</span>
      <span class="network">Posti</span>
      <span class="network">Boost</span>
    </div>
    <div class="footer-rule"></div>
    <p class="copyright">© 2011 zMatchy. All Rights Reserved</p>
    <nav class="footer-links">
      <a href="#">Home</a><a href="#">Why</a><a href="#">How It Works</a><a href="#">Sign Up</a><a href="#">Our Blog</a>
    </nav>
  </footer>
</div>
</body>
</html>
```